Either a trifold or double sided flyer/brochure

A flyer to help spark interest in a historic preservation project in Peterborough, NH--looking for something that captures the early 19th century rural village and mill times--American Primitive, Shaker, Cross Stitch Sampler...must be able to highlight home history as well as have all owners of house on a single page. Word document attached--can also provide files for the house painting, color photos, dorne photo, advertising photo or part of original settler map.
I like this brochure
http://tessavolkind.com/wordpress/quarnby-lodge-museum-brochure/
community stakeholders, residents,
Historic Preservation, House Museums.

```html
<!DOCTYPE html>
<html lang="en">
<head>
<meta charset="utf-8">
<title>The Ashcombe Homestead History c. 1826</title>
<link rel="stylesheet" href="https://fonts.googleapis.com/css2?family=Oswald:wght@500&family=Arimo:wght@400&display=swap">
<style>
  :root {
    --bg: #8a8a8c;
    --navy: #13233a;
    --paper: #f1e9e4;
    --paper-edge: #e8ddd7;
    --gold: #c48a2e;
    --ink: #1d2330;
    --rule: #d9cec8;
    --white: #ffffff;
    --autumn-a: #4a3c24;
    --autumn-b: #8c7038;
    --winter-a: #77797b;
    --winter-b: #b9b7aa;
    --sepia: #6d6253;
    --sepia-dark: #574a3a;
    --painting: #4f5f78;
    --wood: #9b7a58;
    --sky-gold: #9aa07a;
    --map: #dcd8d0;
    --newsprint: #ebe7de;
  }
  * { margin: 0; padding: 0; box-sizing: border-box; }
  html, body { width: 1200px; height: 798px; overflow: hidden; background: var(--bg); }
  .spread { position: relative; width: 1200px; height: 798px; }
  .page {
    position: absolute; top: 84px; width: 487px; height: 630px;
    background: var(--navy); overflow: hidden;
    font-family: "Arimo", Arial, sans-serif; color: var(--ink);
  }
  .page--history { left: 93px; }
  .page--owners { left: 620px; }

  .hero { position: absolute; left: 0; top: 0; width: 487px; height: 190px; }
  .hero--autumn { background: linear-gradient(180deg, var(--autumn-a), var(--autumn-b)); }
  .hero--winter { background: linear-gradient(180deg, var(--winter-a), var(--winter-b)); }

  .paper {
    position: absolute; left: 16px; top: 172px; width: 449px; height: 398px;
    background: linear-gradient(180deg, var(--paper-edge) 0%, var(--paper) 20%, var(--paper) 100%);
  }
  .torn { position: absolute; left: 16px; top: 569px; width: 449px; height: 24px; }

  .title {
    position: absolute; left: 27px; top: 36px;
    font-family: "Oswald", "Arial Narrow", sans-serif; font-weight: 500;
    color: var(--white); font-size: 25px; line-height: 27px; letter-spacing: -0.8px;
    text-transform: uppercase;
  }
  .subtitle {
    position: absolute; left: 27px; top: 128px;
    font-family: "Oswald", "Arial Narrow", sans-serif; font-weight: 500;
    color: var(--white); font-size: 12.5px; letter-spacing: -0.4px; text-transform: uppercase;
  }
  .section-head {
    position: absolute; left: 27px;
    font-family: "Oswald", "Arial Narrow", sans-serif; font-weight: 500;
    color: var(--gold); font-size: 11px; line-height: 12px; letter-spacing: -0.4px; text-transform: uppercase;
  }
  .page--history .section-head { top: 207px; }
  .page--owners .section-head { left: 33px; top: 203px; }

  .story {
    position: absolute; left: 27px; top: 236px; width: 428px;
    font-size: 6.8px; line-height: 9.4px; text-align: justify;
  }
  .story p { margin-bottom: 6px; }

  .snapshot {
    position: absolute; background: var(--white); padding: 5px 5px 11px;
    box-shadow: 1px 2px 4px rgba(0,0,0,.35);
  }
  .snapshot .fill { width: 100%; height: 100%; }
  .snapshot--couple { left: 267px; top: 134px; width: 107px; height: 86px; transform: rotate(-8deg); }
  .snapshot--couple .fill { background: var(--sepia); }
  .snapshot--portrait { left: 374px; top: 150px; width: 104px; height: 86px; transform: rotate(6deg); }
  .snapshot--portrait .fill { background: var(--sepia-dark); }
  .snapshot--painting { left: 322px; top: 122px; width: 154px; height: 122px; transform: rotate(3deg); padding-bottom: 13px; }
  .snapshot--painting .fill { background: var(--painting); }
  .snapshot--stair { left: 331px; top: 250px; width: 92px; height: 62px; transform: rotate(-4deg); padding-bottom: 6px; }
  .snapshot--stair .fill { background: var(--wood); }
  .snapshot--gable { left: 377px; top: 274px; width: 95px; height: 78px; transform: rotate(6deg); padding-bottom: 6px; }
  .snapshot--gable .fill { background: var(--sky-gold); }

  .owners { position: absolute; left: 34px; top: 240px; width: 281px; list-style: none; }
  .owners li {
    position: relative; height: 28.6px; display: flex; align-items: center;
    border-bottom: 0.6px solid var(--rule); font-size: 7.2px; line-height: 8.6px;
  }
  .owners li:last-child { border-bottom: none; }
  .owners .name { width: 232px; }
  .owners .years { color: var(--gold); font-size: 8px; }

  .caption {
    position: absolute; left: 342px; top: 368px; width: 122px;
    text-align: center; font-size: 7.6px; line-height: 10.5px; color: var(--navy);
  }
  .settler-map {
    position: absolute; left: 347px; top: 406px; width: 113px; height: 106px;
    background: var(--map); border: 1px solid #9c9790;
  }
  .mill-advert {
    position: absolute; left: 378px; top: 526px; width: 70px; height: 40px;
    background: var(--newsprint);
  }

  .invite {
    position: absolute; left: 22px; top: 598px; display: flex; align-items: center; gap: 9px;
    color: var(--gold); font-size: 7.8px;
  }
  .invite .dot { width: 24px; height: 24px; border-radius: 50%; background: var(--gold); }
</style>
</head>
<body>
<main class="spread">

  <section class="page page--history">
    <div class="hero hero--autumn" role="img" aria-label="Photo of the yellow clapboard homestead and barn among autumn trees"></div>
    <h1 class="title">The Ashcombe<br>Homestead<br>History c. 1826</h1>
    <p class="subtitle">Peterborough, New Hampshire</p>

    <div class="paper"></div>
    <svg class="torn" viewBox="0 0 449 24" preserveAspectRatio="none" aria-hidden="true">
      <path d="M0 0 H449 V10 L440 16 L431 9 L420 18 L409 12 L398 20 L386 11 L374 17 L362 9 L350 19 L338 13 L326 21 L314 10 L302 16 L290 8 L278 18 L266 12 L254 22 L242 11 L230 17 L218 9 L206 19 L194 13 L182 20 L170 10 L158 16 L146 8 L134 18 L122 12 L110 21 L98 10 L86 17 L74 9 L62 19 L50 12 L38 20 L26 11 L14 17 L0 10 Z" fill="#f1e9e4"/>
    </svg>

    <div class="snapshot snapshot--couple"><div class="fill" role="img" aria-label="Old photograph of Fred and Grace Dorne"></div></div>
    <div class="snapshot snapshot--portrait"><div class="fill" role="img" aria-label="Old portrait photograph of a seated woman"></div></div>

    <h2 class="section-head">The Ashcombe Homestead History c. 1826</h2>
    <div class="story">
      <p>In 1826, George S. Ashcombe and his wife, Jane (Pell) Ashcombe purchased 26 acres from Robert Tenney on the Contoocook River, north of Barrows's Woolen Mill in South Peterborough, NH. This parcel was carved out of lot #32 which was comprised of 268 acres that were deeded to John Tenney (Robert Tenney's grandfather) by Jeremiah Holbrook and John Marsh on May 5, 1762.</p>
      <p>It is believed that Ashcombe, who was blacksmith, built the house that currently stands at 214 Mill Street in Peterborough, NH. He also built his forge on the site down by the river. It is likely that much of the forged hardware in the home was crafted by him. Feeling the need to leave Peterborough for a new frontier, Ashcombe left town with his brother, Ridley, to purchase land in the emerging communities of Orleans County, NY. Before doing so, Ashcombe sold the home, shop and buildings to Thomas Hadley and his wife Alice (Wright) Hadley in 1828.</p>
      <p>By trade, Thomas Hadley was a cloth dresser and wool-carder. He was also a deeply religious man and served as deacon in the emerging, but still quite small, Baptist community. In those days, small groups of the Baptists and Methodists met in the Corliss Home for bible study, prayers and singing. The Corlisses were well known abolitionists and their house served as a stop on the Underground Railroad. Deacon Hadley died in 1839 and his estate was managed by Samuel Wright&mdash;very likely a relative of Alice&mdash;who protected Alice's dower. The property was then sold to Elijah Brown Whitcomb and his wife Achsah (Pratt) Whitcomb. Elijah was quite industrious and continued to expand the wool mill. He was an early investor in the Ridgeline Railroad and ceded a right of way to the railroad on the homestead. The mill eventually came under the control of his son, Henry A. Whitcomb, and operated until it burned down on April 20, 1874. Elijah passed away in 1877 and left the home to Mary Ellen Whitcomb who was most commonly known as &ldquo;Ellen.&rdquo;</p>
      <p>Ellen Whitcomb was approached in 1891 by Allie Barrows, the owner of the Barrows's Mill Complex, to ask if she would be willing to rent out the home to a couple from Boston. This turned out to be Marian and Edward Lindqvist, the founders of the Lindqvist Colony, who ended up spending their first summer in Peterborough, NH in the home. Marian recalls in her writings: &ldquo;You can't fail to remember the two-story farmhouse almost across from the road from the iron bridge, now occupied by the Dorne Family. It had never been painted and was a lovely soft gray in color. There were really only four rooms and a kitchen, spotlessly clean and adequately furnished, which really didn't mean much but some chairs, tables and beds. Then in the kitchen was something that fascinated me, a stone bowl into which the clearest of water was all the time pouring and then running off into a a drain....&rdquo;</p>
      <p>The Dornes lived in this home for the longest time of any owner&mdash;and some refer to this area before the bridge, as Dornes Corner. This moment of stewardship began under Fred Parker Dorne and his wife Grace E. (Lathrop) Dorne around 1904 and lasted until 2015 when a descendant sold the home. The house is now under the stewardship of Edward M. Serrano and Albert A. Prescott, Jr. and will be undergoing a significant restoration.</p>
    </div>

    <div class="invite"><span class="dot"></span><span>They invite you to join their Commonplace Group</span></div>
  </section>

  <section class="page page--owners">
    <div class="hero hero--winter" role="img" aria-label="Photo of the yellow homestead and barn in falling snow"></div>

    <div class="paper"></div>
    <svg class="torn" viewBox="0 0 449 24" preserveAspectRatio="none" aria-hidden="true">
      <path d="M0 0 H449 V12 L437 18 L425 10 L413 19 L401 12 L389 21 L377 11 L365 17 L353 9 L341 19 L329 12 L317 20 L305 10 L293 16 L281 9 L269 18 L257 12 L245 21 L233 11 L221 17 L209 9 L197 19 L185 12 L173 20 L161 10 L149 16 L137 8 L125 18 L113 12 L101 21 L89 10 L77 17 L65 9 L53 19 L41 12 L29 20 L17 11 L0 16 Z" fill="#f1e9e4"/>
    </svg>

    <h2 class="section-head">Of 214 Mill Street<br>Peterborough, New Hampshire</h2>

    <ul class="owners">
      <li><span class="name">Robert Tenney (grandson of John Tenney) owned the land</span><span class="years">1826</span></li>
      <li><span class="name">George S. Ashcombe and Jane (Pell) Ashcombe</span><span class="years">1826-1828</span></li>
      <li><span class="name">Deacon Thomas Hadley and Alice (Wright) Hadley (Baptist)</span><span class="years">1828-1839</span></li>
      <li><span class="name">Elijah Brown Whitcomb and Achsah (Pratt) Whitcomb<br>(mortgage between Samuel Wright and Whitcomb is 1845)</span><span class="years">1839-1877</span></li>
      <li><span class="name">Mary Ellen Whitcomb</span><span class="years">1877-1898</span></li>
      <li><span class="name">James Farrow</span><span class="years">1898-1904</span></li>
      <li><span class="name">Fred Parker Dorne and Grace E. (Lathrop) Dorne</span><span class="years">1904-1956</span></li>
      <li><span class="name">Elinor (Dorne) Halloway and Frank O Halloway<br>(Elinor was born in house on July 29, 1911)</span><span class="years">1956-1998</span></li>
      <li><span class="name">James H. Brandmeier and Maria Sola Brandmeier<br>(James was nephew of Elinor (Dorne) Halloway)</span><span class="years">1998-2015</span></li>
      <li><span class="name">Millbrook Commons</span><span class="years">2015-2022</span></li>
      <li><span class="name">Edward M. Serrano and Albert A. Prescott, Jr.</span><span class="years">2022</span></li>
    </ul>

    <div class="snapshot snapshot--painting"><div class="fill" role="img" aria-label="Painting of the homestead"></div></div>
    <div class="snapshot snapshot--stair"><div class="fill" role="img" aria-label="Photo of the interior wooden staircase"></div></div>
    <div class="snapshot snapshot--gable"><div class="fill" role="img" aria-label="Photo of the gable end of the house"></div></div>

    <p class="caption">Ashcombe Homestead c. 1826,<br>Dornes Corner, Peterborough,<br>New Hampshire</p>
    <div class="settler-map" role="img" aria-label="Section of the original settler map showing the lots"></div>
    <div class="mill-advert" role="img" aria-label="Period newspaper advertisement for the wool carder and cloth dresser"></div>

    <div class="invite"><span class="dot"></span><span>They invite you to join their Commonplace Group</span></div>
  </section>

</main>
</body>
</html>
```